Bayridge Outing Cruises and Charters

I'm looking to update my current website that was written in Joomla. I would like to move to a more modern design that works well on all platforms using a Wordpress theme. The website is, https://www.bayridgecruisesandcharters.example/ It should be noted that I currently have an online booking API (Dockwise) that is integrated with the site but I don't want to worry about that for now. Once I get the new site up and running I am going to move to Tidl which doesn't hook into the site, it just links to an external booking company. Just ignore the Dockwise booking (Book Now) code and build the site. IMPORTANT: My website is hosted on HostMoor and I currently manage it through cPanel. I want to be able to make changes, updates and manage the website once its completed.

Target Market(s)

Tourists visiting Marlow Reef and Venice Florida for Dolphin, sunset tours and private half and full day charters to Pelbrook Isle.

Industry/Entity Type

Tourism

Coding

Coded - Design and coding required

Font styles to use
Other font styles liked:
• Freebooter

Colors
0455a3
85acd3
fbed22
fbee3e
ffc214
ffcf3e
f78f20
faa54b

Requirements
Must have
• Our brand is fun on the water. Social Media links. Great photos, we will provide, and compelling descriptions of each of the tours we offer.
• Dolphin Tours
• Sunset Tours
• Shelling and Snorkeling
• Boating Instruction - I would like this page to have a more professional look and feel. It needs to stand out from the other pages as a professional service yet it still needs to blend well with the entire site.
• What can you do to make this site, https://www.bayridgecruisesandcharters.example/ better?
• I don't really need a "Gallery Page" but I want to highlight lots of great pics from our tours. Here is a good example..... check this site out.
• https://wavinacruises.example/
• I don't want to be "like" Wavina Charters, I want my site to be better. This is my competitor.
Nice to have
• I selected some colors for the theme but basically I just want it to be a bright, fun and outgoing site.
• There is a font you can download called Freebooter. It gives it that Pirate look and feel. I would like to use that in some places. Its in my logo on the website. Don't go overboard with the Pirate look and feel but some subtitle pirate things in the site would make it fun.

```html
<!DOCTYPE html>
<html lang="en">
<head>
<meta charset="utf-8">
<title>Bayridge Outing Cruises and Charters</title>
<link href="https://fonts.googleapis.com/css2?family=Almendra:ital,wght@0,400;0,700;1,400&family=Raleway:wght@400;500;600;700&display=swap" rel="stylesheet">
<style>
:root{
  --blue:#0455a3;
  --blue-deep:#033f7a;
  --sky:#85acd3;
  --sun:#ffc214;
  --orange:#f78f20;
  --ink:#1d1d1d;
  --muted:#4a4a4a;
  --panel:#f1f1f1;
  --white:#ffffff;
  --footer:#2a3944;
}
*{box-sizing:border-box;margin:0;padding:0}
html,body{width:1200px;height:3442px;overflow:hidden}
body{position:relative;font-family:"Raleway",Arial,sans-serif;color:var(--ink);background:var(--white)}
.block{position:absolute;left:0;width:1200px}
.fill{position:absolute;inset:0}
.pill{display:inline-flex;align-items:center;justify-content:center;border-radius:22px;font-size:11px;font-weight:500;color:var(--white);background:var(--blue);box-shadow:0 0 0 2px var(--white),0 0 0 3px var(--sky)}
.pill.light{background:var(--white);color:var(--blue);box-shadow:0 0 0 2px var(--sky)}
.social{display:inline-block;width:15px;height:15px;border-radius:50%;background:var(--white)}

/* hero */
.hero{top:0;height:734px;overflow:hidden}
.hero .fill{background:
  radial-gradient(ellipse 520px 620px at 230px 420px,rgba(190,215,240,.55),rgba(190,215,240,0) 70%),
  radial-gradient(ellipse 600px 260px at 980px 120px,rgba(120,180,230,.55),rgba(120,180,230,0) 70%),
  radial-gradient(ellipse 700px 300px at 800px 640px,rgba(20,70,140,.6),rgba(20,70,140,0) 70%),
  linear-gradient(165deg,#4a8bd0 0%,#2a6fbf 40%,#1c5aa6 75%,#174c8e 100%)}
.topbar-follow{position:absolute;left:220px;top:88px;display:flex;align-items:center;gap:12px;color:var(--white);font-size:12px}
.brand{position:absolute;left:0;width:1200px;top:98px;display:flex;justify-content:center;align-items:center;gap:10px}
.brand-mark{width:26px;height:26px;border-radius:50%;background:var(--sun)}
.brand-name{font-family:"Raleway",Arial,sans-serif;font-weight:700;font-size:30px;color:var(--sun);letter-spacing:1px}
.call{position:absolute;left:822px;top:72px;display:flex;gap:14px;align-items:center;color:var(--white)}
.call b{display:block;font-family:"Almendra",Georgia,serif;font-size:14px;font-weight:400}
.call span{font-size:10px}
.nav{position:absolute;left:142px;top:167px;width:916px;height:60px;background:var(--white);box-shadow:0 3px 8px rgba(0,0,0,.25);display:flex;justify-content:space-around;align-items:center;padding:0 80px;font-family:"Almendra",Georgia,serif;font-size:12px;color:#222}
.hero-copy{position:absolute;left:0;width:1200px;top:334px;text-align:center;color:var(--white)}
.hero-kicker{font-family:"Almendra",Georgia,serif;font-style:italic;font-size:20px}
.hero-title{font-size:40px;font-weight:600;margin-top:22px}
.hero-rule{width:70px;height:2px;background:rgba(255,255,255,.7);margin:14px auto 0}
.hero-text{width:690px;margin:16px auto 0;font-size:11px;line-height:24px}
.hero .pill{margin-top:28px;width:134px;height:42px}
.hero-arrow{position:absolute;top:402px;width:40px;height:40px;border-radius:50%;background:var(--white);display:flex;align-items:center;justify-content:center}

/* tours */
.tours{top:734px;height:707px;text-align:center}
.section-title{font-size:32px;font-weight:600;margin-top:55px}
.section-lead{width:470px;margin:22px auto 0;font-size:11px;line-height:22px;color:var(--muted)}
.tour-card{position:absolute;top:188px;width:288px;height:370px;background:var(--panel)}
.tour-photo{position:absolute;left:13px;top:14px;width:262px;height:158px}
.tour-card h3{position:absolute;top:200px;width:100%;font-size:17px;font-weight:700}
.tour-card p{position:absolute;top:228px;left:36px;right:36px;font-size:10.5px;line-height:24px;color:var(--muted)}
.tour-card .pill{position:absolute;top:308px;left:82px;width:124px;height:38px}
.pager{position:absolute;top:612px;left:0;width:1200px;display:flex;justify-content:center;gap:16px}
.pager span{width:38px;height:38px;border-radius:50%;border:1px solid #ddd;display:flex;align-items:center;justify-content:center;background:#fafafa}

/* sightseeing */
.sights{top:1441px;height:543px;overflow:hidden}
.sights .fill{background:
  radial-gradient(ellipse 260px 160px at 420px 90px,rgba(90,130,165,.55),rgba(90,130,165,0) 70%),
  radial-gradient(ellipse 520px 220px at 260px 330px,rgba(60,100,140,.5),rgba(60,100,140,0) 70%),
  radial-gradient(ellipse 300px 260px at 1150px 330px,rgba(70,80,90,.6),rgba(70,80,90,0) 70%),
  linear-gradient(180deg,#3a6180 0%,#1d3f5f 30%,#13304c 65%,#0c2238 100%)}
.sights-title{position:absolute;left:156px;top:125px;width:380px;font-family:"Almendra",Georgia,serif;font-weight:400;font-size:30px;line-height:54px;color:var(--white)}
.sights-text{position:absolute;left:150px;top:262px;width:360px;font-size:11px;line-height:24px;color:var(--white)}
.sights .pill{position:absolute;left:157px;top:394px;width:128px;height:40px}
.video{position:absolute;left:532px;top:133px;width:526px;height:328px;border:2px solid #cfd8e2;background:
  radial-gradient(ellipse 200px 140px at 60px 40px,rgba(235,245,250,.8),rgba(235,245,250,0) 70%),
  radial-gradient(ellipse 260px 120px at 300px 70px,rgba(190,220,235,.7),rgba(190,220,235,0) 70%),
  radial-gradient(ellipse 420px 150px at 260px 300px,rgba(55,70,90,.7),rgba(55,70,90,0) 70%),
  linear-gradient(180deg,#6fa6c6 0%,#3c7fa6 45%,#2f5f80 100%)}
.play{position:absolute;left:229px;top:130px}

/* testimonials */
.reviews{top:1984px;height:546px;background:#f4f4f4;overflow:hidden}
.reviews-photo{position:absolute;left:0;top:0;width:760px;height:546px;background:
  linear-gradient(90deg,rgba(244,244,244,0) 0%,rgba(244,244,244,0) 72%,#f4f4f4 100%),
  radial-gradient(ellipse 200px 260px at 230px 330px,rgba(240,244,248,.85),rgba(240,244,248,0) 70%),
  radial-gradient(ellipse 130px 180px at 420px 360px,rgba(150,130,190,.55),rgba(150,130,190,0) 70%),
  linear-gradient(180deg,#cfe3f2 0%,#a7cbe6 18%,#3f86b6 26%,#2f78aa 60%,#c8b79a 100%)}
.reviews-title{position:absolute;left:644px;width:400px;top:58px;text-align:center;font-family:"Almendra",Georgia,serif;font-size:30px}
.reviews-rule{position:absolute;left:804px;top:112px;width:82px;height:2px;background:var(--blue)}
.quote-card{position:absolute;left:656px;top:154px;width:402px;height:287px;background:var(--white);border-radius:16px;box-shadow:0 4px 14px rgba(0,0,0,.2);text-align:center}
.quote-mark{font-family:"Almendra",Georgia,serif;font-size:90px;font-weight:700;line-height:1;margin-top:30px;height:70px}
.quote-card p{width:350px;margin:20px auto 0;font-size:11px;line-height:24px;color:var(--muted)}
.quote-card b{display:block;margin-top:16px;font-size:12px}
.reviews .pager{top:461px;left:744px;width:200px;gap:6px}
.reviews .pager span{width:30px;height:30px}

/* offers */
.offers{top:2530px;height:581px}
.offer{position:absolute;top:67px;width:446px;text-align:center}
.offer-frame{height:275px;background:var(--panel);padding:15px}
.offer-photo{width:100%;height:100%}
.offer h3{margin-top:50px;font-family:"Almendra",Georgia,serif;font-weight:400;font-size:19px}
.offer p{margin-top:16px;font-size:11px;color:var(--muted)}
.offer .pill{margin-top:44px;width:128px;height:38px}

/* footer */
.footer{top:3111px;height:296px;color:var(--white)}
.footer .fill{background:
  radial-gradient(ellipse 300px 140px at 640px 90px,rgba(90,120,130,.45),rgba(90,120,130,0) 70%),
  radial-gradient(ellipse 500px 200px at 300px 250px,rgba(60,85,95,.5),rgba(60,85,95,0) 70%),
  linear-gradient(180deg,#38474f,#27343c)}
.footer .brand{left:165px;width:220px;top:126px}
.footer .brand-name{font-size:28px;color:var(--orange)}
.footer .brand-mark{background:var(--orange)}
.footer-social{position:absolute;left:177px;top:208px;width:24px;height:24px;border-radius:50%;background:#3b5fa8}
.footer h4{position:absolute;top:62px;font-family:"Almendra",Georgia,serif;font-weight:400;font-size:17px}
.footer h4::after{content:"";display:block;width:52px;height:1px;background:rgba(255,255,255,.6);margin-top:10px}
.links{position:absolute;top:116px;font-size:11px;line-height:38px}
.contact{position:absolute;left:849px;top:116px;font-size:11px}
.contact li{list-style:none;display:flex;align-items:center;gap:10px;height:38px}
.copyright{top:3407px;height:35px;background:var(--blue);color:var(--white);font-size:11px;display:flex;align-items:center;justify-content:center}
</style>
</head>
<body>

<header class="block hero">
  <div class="fill" role="img" aria-label="Tour boat on blue bay water under a blue overlay"></div>
  <div class="topbar-follow">Follow Us On: <span class="social"></span><span class="social"></span><span class="social"></span></div>
  <div class="brand"><span class="brand-mark"></span><span class="brand-name">BAYRIDGE</span></div>
  <div class="call">
    <svg width="20" height="20" viewBox="0 0 24 24"><circle cx="12" cy="12" r="12" fill="#fff"/><path d="M8 6l2 0 1 3-1.5 1a7 7 0 0 0 4.5 4.5L15 13l3 1v2a2 2 0 0 1-2 2A10 10 0 0 1 6 8a2 2 0 0 1 2-2z" fill="#0455a3"/></svg>
    <div><b>Call Now!</b><span>555.014.2760</span></div>
  </div>
  <nav class="nav"><span>Home</span><span>Dolphin Tours</span><span>Sunset Tours</span><span>Shelling and Snorkeling</span><span>Boating Instruction</span><span>Contact Us</span></nav>
  <div class="hero-copy">
    <div class="hero-kicker">Explore The</div>
    <h1 class="hero-title">Marlow Reef and Venice's #1 Dolphin Tour</h1>
    <div class="hero-rule"></div>
    <p class="hero-text">Lorem ipsum dolor sit amet, consectetur adipiscing elit, sed do eiusmod tempor incididunt ut labore et dolore magna aliqua. Ut enim ad minim veniam, quis nostrud exercitation.</p>
    <span class="pill">Let Go!</span>
  </div>
  <span class="hero-arrow" style="left:72px"><svg width="10" height="12"><path d="M8 1L2 6l6 5" stroke="#333" stroke-width="2" fill="none"/></svg></span>
  <span class="hero-arrow" style="left:1086px"><svg width="10" height="12"><path d="M2 1l6 5-6 5" stroke="#333" stroke-width="2" fill="none"/></svg></span>
</header>

<section class="block tours">
  <h2 class="section-title">Bayridge Outing Cruises and Charters</h2>
  <p class="section-lead">Lorem ipsum dolor sit amet, consectetur adipiscing elit, sed do eiusmod tempor incididunt ut labore et dolore magna aliqua.</p>
  <article class="tour-card" style="left:142px">
    <div class="tour-photo" role="img" aria-label="Dolphin surfacing in green water" style="background:radial-gradient(ellipse 90px 70px at 130px 70px,rgba(200,215,210,.75),rgba(200,215,210,0) 70%),radial-gradient(ellipse 200px 120px at 40px 20px,#6cc0ae,rgba(108,192,174,0) 70%),linear-gradient(160deg,#4fae9b,#2a8272 60%,#1f6c60)"></div>
    <h3>Dolphin Tours</h3>
    <p>Lorem ipsum dolor sit amet, consectetur adipiscing elit.</p>
    <span class="pill">Let Go!</span>
  </article>
  <article class="tour-card" style="left:455px">
    <div class="tour-photo" role="img" aria-label="Sailboat at sunset over the gulf" style="background:radial-gradient(ellipse 160px 50px at 110px 92px,#ffd27a,rgba(255,180,80,0) 70%),linear-gradient(180deg,#44516d 0%,#8a6a5c 35%,#e59a3e 55%,#c0702a 62%,#3b2c22 78%,#1b1612 100%)"></div>
    <h3>Sunset Tours</h3>
    <p>Lorem ipsum dolor sit amet, consectetur adipiscing elit.</p>
    <span class="pill">Let Go!</span>
  </article>
  <article class="tour-card" style="left:768px">
    <div class="tour-photo" role="img" aria-label="Seashell resting on white sand" style="background:radial-gradient(ellipse 40px 26px at 132px 86px,#c57a4a,rgba(197,122,74,0) 80%),radial-gradient(ellipse 220px 110px at 130px 60px,#f2efe9,rgba(242,239,233,0) 70%),linear-gradient(160deg,#e6e2da,#c9c3b8)"></div>
    <h3>Shelling and Snorkeling</h3>
    <p>Lorem ipsum dolor sit amet, consectetur adipiscing elit.</p>
    <span class="pill">Let Go!</span>
  </article>
  <div class="pager">
    <span><svg width="8" height="10"><path d="M6 1L2 5l4 4" stroke="#aaa" stroke-width="1.5" fill="none"/></svg></span>
    <span><svg width="8" height="10"><path d="M2 1l4 4-4 4" stroke="#aaa" stroke-width="1.5" fill="none"/></svg></span>
  </div>
</section>

<section class="block sights">
  <div class="fill" role="img" aria-label="Dolphin fin breaking the surface of dark open water"></div>
  <svg class="fill" width="1200" height="543" viewBox="0 0 1200 543" preserveAspectRatio="none"><path d="M0 0H1200V20C1000 52 850 6 650 30S250 28 0 36Z" fill="#fff"/></svg>
  <h2 class="sights-title">Dolphin Sightseeing and Sunset Tours!</h2>
  <p class="sights-text">Our goal is for you to have your best vacation day ever, so let us take care of your adventure. We offer sightseeing tours, evening boat rides or special event services. It's your adventure, let us take you there.</p>
  <span class="pill light">Read More</span>
  <div class="video" role="img" aria-label="Video still of guests smiling aboard the boat">
    <svg class="play" width="68" height="68" viewBox="0 0 68 68"><circle cx="34" cy="34" r="31" fill="none" stroke="#fff" stroke-width="4"/><path d="M27 21l20 13-20 13z" fill="#fff"/></svg>
  </div>
</section>

<section class="block reviews">
  <div class="reviews-photo" role="img" aria-label="Captain and young guest seated on a boat at sea"></div>
  <h2 class="reviews-title">Testimonials</h2>
  <div class="reviews-rule"></div>
  <blockquote class="quote-card">
    <div class="quote-mark">&ldquo;</div>
    <p>Lorem ipsum dolor sit amet, consectetur adipiscing elit, sed do eiusmod tempor incididunt ut labore et dolore magna aliqua. Ut enim ad minim veniam, quis nostrud</p>
    <b>Name Here</b>
  </blockquote>
  <div class="pager">
    <span><svg width="8" height="10"><path d="M6 1L2 5l4 4" stroke="#aaa" stroke-width="1.5" fill="none"/></svg></span>
    <span><svg width="8" height="10"><path d="M2 1l4 4-4 4" stroke="#aaa" stroke-width="1.5" fill="none"/></svg></span>
  </div>
</section>

<section class="block offers">
  <article class="offer" style="left:142px">
    <div class="offer-frame"><div class="offer-photo" role="img" aria-label="Charter yacht cruising with a dolphin alongside" style="background:radial-gradient(ellipse 160px 60px at 290px 70px,rgba(245,245,245,.85),rgba(245,245,245,0) 70%),radial-gradient(ellipse 120px 40px at 140px 170px,rgba(220,240,240,.6),rgba(220,240,240,0) 70%),linear-gradient(180deg,#b9d9ec 0%,#9cc8df 16%,#4a9a98 24%,#2f8581 60%,#236e6a 100%)"></div></div>
    <h3>Custom Destination Charter</h3>
    <p>We'll get you to that perfect spot for the day!</p>
    <span class="pill">Book Now</span>
  </article>
  <article class="offer" style="left:612px">
    <div class="offer-frame"><div class="offer-photo" role="img" aria-label="Gift box wrapped with a red ribbon bow" style="background:radial-gradient(ellipse 120px 90px at 270px 80px,rgba(220,40,40,.55),rgba(220,40,40,0) 70%),linear-gradient(135deg,#fdfaf0,#f5eedb)"></div></div>
    <h3>Gift Card</h3>
    <p>Lorem ipsum dolor sit amet, consectetur adipiscing elit</p>
    <span class="pill">Buy Card</span>
  </article>
</section>

<footer class="block footer">
  <div class="fill" role="img" aria-label="Faint photo of a dolphin in the water behind a dark overlay"></div>
  <div class="brand"><span class="brand-mark"></span><span class="brand-name">BAYRIDGE</span></div>
  <span class="footer-social"></span>
  <h4 style="left:525px">Quick Links</h4>
  <div class="links" style="left:525px">&rsaquo;&nbsp; Home<br>&rsaquo;&nbsp; Dolphin Tours<br>&rsaquo;&nbsp; Sunset Tours</div>
  <div class="links" style="left:672px">&rsaquo;&nbsp; Shelling and Snorkeling<br>&rsaquo;&nbsp; Boating Instruction<br>&rsaquo;&nbsp; Contact Us</div>
  <h4 style="left:849px">Contact Us</h4>
  <ul class="contact">
    <li><svg width="12" height="12" viewBox="0 0 24 24"><path d="M6 2l4 0 2 6-3 2a12 12 0 0 0 5 5l2-3 6 2v4a3 3 0 0 1-3 3A19 19 0 0 1 3 5a3 3 0 0 1 3-3z" fill="#fff"/></svg>555.014.2760</li>
    <li><svg width="12" height="10" viewBox="0 0 24 18"><rect width="24" height="18" rx="2" fill="#fff"/><path d="M1 2l11 8 11-8" stroke="#2a3944" stroke-width="2" fill="none"/></svg>hello@bayridgecruises.example</li>
    <li><svg width="10" height="13" viewBox="0 0 20 26"><path d="M10 0a10 10 0 0 1 10 10c0 7-10 16-10 16S0 17 0 10A10 10 0 0 1 10 0z" fill="#fff"/><circle cx="10" cy="10" r="4" fill="#2a3944"/></svg>123 Lorem Ipsum,City name</li>
  </ul>
</footer>
<div class="block copyright">Copyright &copy; 2019 Bayridge</div>

</body>
</html>
```